Interior Styling Workshop needs a brochure designed.

Hue Harbor is an interior design firm based in Sydney. We will be running Interior Styling Workshops
for all people interested in learning how to decorate
their home. It is important to show modern interior images to attract and excite their creative juices!
Colours we would like is a dark charcoal background
with Chartreuse trim for our logo and for the brochure.
We have attached some of our ideas on wording.
Our images can be replaced or changed to suit your
design.
The final design should be very stylish and to instill a desire to attend our workshops!

Target Market(s)

Mainly female adults in Sydney, aged approx. 25 to 60, who are interested in
interior decorating their homes.

Industry/Entity Type

Learning

Colors
5c5c5c
acd036

Requirements
Must have
• Must show good visual images to catch attention.
Nice to have
• Page layout i.e. to uploaded document, but open to any designs that work better.

```html
<!DOCTYPE html>
<html lang="en">
<head>
<meta charset="utf-8">
<title>Hue Harbor – Interior Styling Workshops</title>
<link rel="stylesheet" href="https://fonts.googleapis.com/css2?family=Roboto+Condensed:wght@400;700&display=swap">
<style>
  :root {
    --stage: #dcdcdc;
    --charcoal: #4a4a4a;
    --charcoal-deep: #3c3c3c;
    --panel: #555555;
    --panel-soft: rgba(80, 80, 80, 0.85);
    --chartreuse: #acd036;
    --white: #ffffff;
    --ink: #111111;
  }
  * { box-sizing: border-box; margin: 0; padding: 0; }
  html, body { width: 1200px; height: 1000px; overflow: hidden; }
  body {
    background: var(--stage);
    font-family: "Roboto Condensed", "Arial Narrow", sans-serif;
    position: relative;
  }
  .brochure {
    position: absolute;
    left: 78px; top: 94px;
    width: 1045px; height: 812px;
    background: radial-gradient(circle at 30% 40%, #545454 0%, var(--charcoal) 55%, var(--charcoal-deep) 100%);
    overflow: hidden;
  }
  .trim { position: absolute; inset: 0; width: 100%; height: 100%; pointer-events: none; }
  .brand-mark {
    position: absolute; left: 8px; top: 10px; width: 87px; height: 102px;
    background: var(--panel);
    border: 2px solid #d8d8d8;
    display: flex; align-items: center; justify-content: center; text-align: center;
  }
  .brand-name { color: var(--chartreuse); font-weight: 400; font-size: 21px; line-height: 1.05; }
  .checklist { position: absolute; left: 22px; top: 155px; width: 320px; list-style: none; }
  .checklist li {
    display: flex; align-items: flex-start; gap: 8px;
    color: var(--white); font-size: 19.5px; line-height: 23px; letter-spacing: 0.2px;
    margin-bottom: 20px;
  }
  .checklist li .tick { flex: 0 0 22px; margin-top: 1px; }
  .checklist li span { background: var(--panel-soft); padding: 2px 4px; }
  .photo {
    position: absolute;
    border: 2px solid var(--chartreuse);
  }
  .photo--purple-bedroom { left: 350px; top: 17px; width: 350px; height: 250px; background: linear-gradient(160deg, #c3b4cf 0%, #7a3f86 45%, #e8e2ea 100%); }
  .photo--orange-kitchen { left: 352px; top: 267px; width: 185px; height: 142px; background: linear-gradient(180deg, #eeeeee 0%, #e9893a 60%, #c7c7c7 100%); }
  .photo--green-bathroom { left: 537px; top: 267px; width: 163px; height: 205px; background: linear-gradient(160deg, #7bb13c 0%, #5a9a2c 60%, #dcdcd0 100%); }
  .photo--dining-room { left: 352px; top: 409px; width: 213px; height: 150px; background: linear-gradient(180deg, #b7aea5 0%, #6a5d55 60%, #3a2f2a 100%); }
  .photo--warm-bedroom { left: 565px; top: 472px; width: 135px; height: 165px; background: linear-gradient(170deg, #e3c28d 0%, #b98846 55%, #6a3f1e 100%); }
  .photo--white-bedding { left: 38px; top: 610px; width: 192px; height: 194px; background: linear-gradient(180deg, #f2f2f0 0%, #c9c9c7 55%, #9e9e9c 100%); }
  .photo--seaside-bedroom { left: 230px; top: 549px; width: 309px; height: 255px; background: linear-gradient(180deg, #6cb7de 0%, #cfe9f6 38%, #e7466c 65%, #f2f2f2 100%); }
  .photo--living-room { left: 537px; top: 637px; width: 230px; height: 167px; background: linear-gradient(160deg, #f0d9b5 0%, #e46a2b 35%, #e9d8bf 75%, #b48a55 100%); }
  .photo--brown-bedroom { left: 765px; top: 637px; width: 230px; height: 167px; background: linear-gradient(170deg, #e6d6c2 0%, #9a4f27 50%, #7a5a44 100%); }
  .portrait-slot {
    position: absolute; top: 44px; width: 123px; height: 140px;
    background: var(--white);
    display: flex; align-items: center; justify-content: center;
    color: var(--ink); font-size: 19px;
  }
  .portrait-slot--first { left: 747px; }
  .portrait-slot--second { left: 883px; }
  .intro {
    position: absolute; left: 723px; top: 210px; width: 317px; height: 412px;
    background: var(--panel);
    padding: 6px 10px 0 10px;
    color: var(--white); font-size: 17.6px; line-height: 25.6px;
    text-align: justify; hyphens: auto;
  }
  .intro strong { color: var(--chartreuse); font-weight: 400; font-size: 24.5px; line-height: 31px; }
</style>
</head>
<body>
  <main class="brochure">
    <svg class="trim" viewBox="0 0 1045 812" aria-hidden="true">
      <polygon points="0,0 1022,0 1016,8 0,8" fill="var(--chartreuse)"/>
      <rect x="0" y="0" width="5" height="812" fill="var(--chartreuse)"/>
      <polygon points="1045,650 1045,812 1030,812 1030,662" fill="var(--chartreuse)"/>
      <line x1="349" y1="8" x2="349" y2="549" stroke="var(--chartreuse)" stroke-width="2"/>
      <line x1="702" y1="8" x2="702" y2="637" stroke="var(--chartreuse)" stroke-width="2"/>
    </svg>

    <div class="brand-mark"><span class="brand-name">Hue<br>Harbor</span></div>

    <ul class="checklist">
      <li><svg class="tick" width="22" height="20" viewBox="0 0 22 20"><rect x="1" y="3" width="15" height="15" fill="none" stroke="var(--chartreuse)" stroke-width="2"/><path d="M5 10 l4 4 l11 -13" fill="none" stroke="var(--chartreuse)" stroke-width="3"/></svg><span>Would you like to transform your home?</span></li>
      <li><svg class="tick" width="22" height="20" viewBox="0 0 22 20"><rect x="1" y="3" width="15" height="15" fill="none" stroke="var(--chartreuse)" stroke-width="2"/><path d="M5 10 l4 4 l11 -13" fill="none" stroke="var(--chartreuse)" stroke-width="3"/></svg><span>Do you feel overwhelmed and confused as to Where to start?</span></li>
      <li><svg class="tick" width="22" height="20" viewBox="0 0 22 20"><rect x="1" y="3" width="15" height="15" fill="none" stroke="var(--chartreuse)" stroke-width="2"/><path d="M5 10 l4 4 l11 -13" fill="none" stroke="var(--chartreuse)" stroke-width="3"/></svg><span>Are you unsure of a colour scheme, what type of furniture, Soft furnishings, accessories suit your home and lifestyle?</span></li>
      <li><svg class="tick" width="22" height="20" viewBox="0 0 22 20"><rect x="1" y="3" width="15" height="15" fill="none" stroke="var(--chartreuse)" stroke-width="2"/><path d="M5 10 l4 4 l11 -13" fill="none" stroke="var(--chartreuse)" stroke-width="3"/></svg><span>Where to buy? What will suit your budget?</span></li>
    </ul>

    <div class="photo photo--purple-bedroom" role="img" aria-label="Modern bedroom with purple feature wall, white bed and chandelier"></div>
    <div class="photo photo--orange-kitchen" role="img" aria-label="Kitchen with glossy orange cabinets and steel rangehood"></div>
    <div class="photo photo--green-bathroom" role="img" aria-label="Bathroom with lime green walls and floating vanity"></div>
    <div class="photo photo--dining-room" role="img" aria-label="Elegant dining room with dark table and crystal pendant"></div>
    <div class="photo photo--warm-bedroom" role="img" aria-label="Warm toned bedroom with timber chest of drawers and vase"></div>
    <div class="photo photo--white-bedding" role="img" aria-label="Bed dressed in white and grey linen with cushions"></div>
    <div class="photo photo--seaside-bedroom" role="img" aria-label="Bright bedroom with ocean view and pink bedspread"></div>
    <div class="photo photo--living-room" role="img" aria-label="Living room with orange curtains and cream sofa"></div>
    <div class="photo photo--brown-bedroom" role="img" aria-label="Bedroom with cherry timber bed and wardrobe"></div>

    <div class="portrait-slot portrait-slot--first">PHOTO</div>
    <div class="portrait-slot portrait-slot--second">PHOTO</div>

    <p class="intro"><strong>Tessa Morgan and Claire Whitfield of HUE HARBOR Interior Design</strong> understand the frustration and confusion that D.I.Y. home decorators face and will be holding INTERIOR STYLING WORKSHOPS in which you will learn how to create innovative colour schemes and styles from concept to completion in a fun, hands on experience, surrounded by beautiful furniture, fabrics, soft furnishings and homewares that will get your creative juices flowing!</p>
  </main>
</body>
</html>
```